Bubble map/flip book

I need someone to create a bubble map with explanations using the attached. This will be used to create a color coded flip book/manual. I need you to clean this up.

Dorothywinslade@postlark.com

```html
<!DOCTYPE html>
<html lang="en">
<head>
<meta charset="utf-8">
<title>Claim Denial Guide</title>
<link href="https://fonts.googleapis.com/css2?family=Ubuntu:wght@400;500;700&display=swap" rel="stylesheet">
<style>
:root{
  --bg:#ffffff;
  --page:#f1f1f1;
  --page-edge:#d9d9d9;
  --red:#e8000a;
  --red-dark:#b80008;
  --yellow:#ffe600;
  --yellow-deep:#f3b400;
  --orange:#f29100;
  --line:#8c8c8c;
  --ink:#3b3b3b;
  --ink-red:#b3261e;
  --gold:#e5b600;
  --green:#1fcc12;
  --magenta:#d616d0;
  --purple:#7d24d6;
  --blue:#1e74e6;
  --orange-ring:#ef7a00;
  --ring-red:#e2222a;
  --lime:#63d41a;
  --pink:#d21ec8;
}
*{box-sizing:border-box;margin:0;padding:0}
html,body{width:927px;height:1200px;overflow:hidden;background:var(--bg)}
body{position:relative;font-family:'Ubuntu',sans-serif;color:var(--ink)}
.page{position:absolute;left:242px;width:444px;height:574px;
  background:radial-gradient(ellipse at 50% 35%,#fafafa 0%,#ececec 70%,#e2e2e2 100%);
  box-shadow:2px 3px 5px rgba(0,0,0,.35)}
.page--overview{top:26px}
.page--auth{top:616px}
.page__band{position:absolute;left:0;top:0;width:100%;height:31px}
.page--overview .page__band{background:linear-gradient(90deg,#ff0a0a,#f20000 60%,#c40006)}
.page--auth .page__band{height:30px;background:linear-gradient(180deg,#ffe600 0%,#f7cf00 75%,#e2a900 100%)}
.page__fold{position:absolute;right:18px;bottom:16px;width:46px;height:48px}
.links{position:absolute;left:0;top:0;width:927px;height:1200px}
.pill{position:absolute;left:308px;width:310px;border-radius:40px;text-align:center;color:#fff;font-weight:700;
  box-shadow:0 3px 5px rgba(0,0,0,.3)}
.pill--red{top:142px;height:66px;padding-top:15px;font-size:24px;
  background:linear-gradient(180deg,#ff3b3b,#e80010 55%,#c90010);border:5px solid #fff;outline:3px solid var(--red);
  letter-spacing:.3px}
.pill--gold{top:666px;height:64px;padding-top:10px;font-size:16px;line-height:21px;
  background:linear-gradient(180deg,#ffd23a,#f2a900 55%,#d98d00);border:4px solid #fff;outline:3px solid var(--yellow-deep);
  text-shadow:0 0 2px #8a5200,1px 1px 1px #7a4800}
.bubble{position:absolute;width:80px;height:80px;margin:-40px 0 0 -40px;border-radius:50%;
  display:flex;align-items:center;justify-content:center;text-align:center;font-size:12.5px;line-height:13px;color:var(--ink);
  border:6px solid var(--c);background:radial-gradient(circle at 50% 40%,#fff 40%,#e4e4e4 100%);
  box-shadow:0 0 0 2px #fff,0 0 0 3px #d0d0d0,1px 3px 5px rgba(0,0,0,.3)}
.bubble--small{font-size:10.5px;line-height:11px}
.note{position:absolute;text-align:center;font-size:8px;line-height:10.4px}
.note--lead{left:407px;top:754px;width:112px;height:66px;padding:18px 4px 0;color:var(--ink-red);
  background:linear-gradient(180deg,#f5a200 0 6px,#fff 6px 7px,#ffe500 7px,#f5cf00);box-shadow:1px 2px 3px rgba(0,0,0,.3)}
.note--lead::before{content:"";position:absolute;left:54px;top:-15px;border:8px solid transparent;border-bottom:8px solid #f5a200;border-left-width:2px}
.card{position:absolute;top:860px;width:128px;height:106px;padding:6px;border-radius:3px;
  background:linear-gradient(180deg,#ffe500,#f4b300 55%,var(--bot));box-shadow:1px 2px 3px rgba(0,0,0,.35)}
.card::before{content:"";position:absolute;left:54px;top:-3px;width:20px;height:5px;border-radius:2px;background:#ffe500}
.card__body{width:100%;height:100%;background:linear-gradient(180deg,#fff,#e9e9e9);border-radius:2px;
  font-size:8px;line-height:10.4px;padding:14px 4px 0;text-align:center}
.card--left{left:282px;--bot:#e04a3f}
.card--right{left:502px;--bot:#8eb81a}
.card--right .card__body{padding-top:12px}
.tile{position:absolute;top:998px;width:95px;height:92px;padding:4px;border-radius:3px;
  background:linear-gradient(180deg,var(--rim) 0 8px,var(--rim2) 100%);box-shadow:1px 2px 3px rgba(0,0,0,.35)}
.tile::before{content:"";position:absolute;left:44px;top:-3px;width:7px;height:7px;border-radius:50%;background:#555}
.tile__body{width:100%;height:100%;background:linear-gradient(180deg,#fff200,#f5d600);
  font-size:8px;line-height:10.4px;text-align:center;padding:3px 3px 0}
.tile--denied,.tile--paid{--rim:var(--pink);--rim2:#8a1a14}
.tile--denied .tile__body,.tile--paid .tile__body{color:#8a2a12}
.tile--review,.tile--carrier{--rim:var(--lime);--rim2:#2aa81a}
.tile--review .tile__body,.tile--carrier .tile__body{color:#555}
.tile--denied{left:252px}.tile--paid{left:359px}.tile--review{left:471px}.tile--carrier{left:579px}
</style>
</head>
<body>
<section class="page page--overview">
  <div class="page__band"></div>
  <svg class="page__fold" viewBox="0 0 46 48"><polygon points="46,0 46,48 0,48" fill="#e8000a"/></svg>
</section>
<section class="page page--auth">
  <div class="page__band"></div>
  <svg class="page__fold" viewBox="0 0 46 48"><polygon points="46,0 46,48 0,48" fill="#ffe600"/></svg>
</section>

<svg class="links" viewBox="0 0 927 1200" fill="none" stroke="#8c8c8c" stroke-width="2">
  <path d="M312 182H300V276"/>
  <path d="M614 176H626V276"/>
  <path d="M355 205V386M409 205V276M463 205V386M517 205V276M573 205V386"/>
  <path d="M463 820V836M346 860V836H566V860"/>
  <path d="M346 966V974M298 998V974H406V998"/>
  <path d="M566 966V974M518 998V974H626V998"/>
</svg>

<div class="pill pill--red">CLAIM HAS DENIED</div>
<div class="bubble" style="left:300px;top:316px;--c:#e3b800">Auth/<br>Referal<br>needed</div>
<div class="bubble" style="left:409px;top:316px;--c:#1fcc12">Duplicate</div>
<div class="bubble" style="left:517px;top:316px;--c:#d616d0">Global<br>Inclusive</div>
<div class="bubble" style="left:626px;top:316px;--c:#ef7a00">Past<br>timely<br>Filing</div>
<div class="bubble" style="left:355px;top:426px;--c:#7d24d6">Coding/<br>Billing<br>Issues</div>
<div class="bubble" style="left:463px;top:426px;--c:#e2222a">Now<br>Covered<br>Charge</div>
<div class="bubble bubble--small" style="left:573px;top:426px;--c:#1e74e6">Additional<br>Informetion<br>Requested</div>

<div class="pill pill--gold">Claim denied for no authorization<br>/referral</div>
<div class="note note--lead">Contract carrier. Was claim processed in network or out of network.</div>

<div class="card card--left"><div class="card__body">Claim has processed correctly as in network provider. Medical records printed and appeal sent for medical necessity</div></div>
<div class="card card--right"><div class="card__body">Claim processed out of network. Contact with Carrier shows claim processed out of network in error.<br><br>Will representative send the claim back for review?</div></div>

<div class="tile tile--denied"><div class="tile__body">Appeal denied as services were not emergent. Balance is patient responsibility.</div></div>
<div class="tile tile--paid"><div class="tile__body">Appeal for claim paid.</div></div>
<div class="tile tile--review"><div class="tile__body">Claim has been sent back for review. Follow uo in 14 days.</div></div>
<div class="tile tile--carrier"><div class="tile__body">Representative will not send the claim back for review. Appeal sent to carrier. followup 30 days.</div></div>
</body>
</html>
```